Website design for a construction company

The logo and the copies of all the 3 pages are attached below. I don't have a preference in colors but I would ideally like to use the colors on my logo, dark teal (secondary) and copper (primary).

Company Name: Torvin Group

Location: London, UK

Business Overview:

Torvin Group is a comprehensive construction company based in London, specializing in a wide range of construction services. We cater to various sectors, providing services including electrical work, painting and decorating, plastering, plumbing, carpentry, kitchen and bathroom installations, loft conversions, and extensions. Our team is known for its skilled craftsmanship, attention to detail, and commitment to quality.

What "TORVIN" stands for:

Our company name, 'TORVIN', is derived from Hephaestus, the ancient Greek god of craftsmen, blacksmiths, artisans, sculptors, metals, metallurgy, fire, and volcanoes. Hephaestus was renowned in mythology for his incredible skill in crafting and creating, making him the patron of all craftsmen and artisans. His name is synonymous with the mastery of artisanship and the creation of wondrous, enduring works.

In choosing 'TORVIN' as our name, we embody the spirit and skills of Hephaestus. It reflects our commitment to craftsmanship, excellence, and durability in the field of construction. Just as Hephaestus was known for his meticulous work, precision, and innovative creations, our company strives to uphold these qualities in every project we undertake.

Our name is a constant reminder of our dedication to quality, innovation, and the art of building. It symbolizes our endeavor to achieve the highest standards in construction, much like Hephaestus did in his timeless creations. In essence, 'TORVIN' is not just our name; it's a representation of our ethos and the high standards we set for ourselves in the construction industry.

Target Audience:

Our primary audience includes homeowners, real estate developers, and commercial clients in London seeking reliable, high-quality construction services.

Unique Selling Points:

Diverse Range of Services: Offering a one-stop solution for all construction needs.

Certified and Experienced: Professional team with a strong focus on delivering certified and compliant work, particularly in electrical services.

Client-Centric Approach: Emphasizing client satisfaction, we tailor our services to meet the unique needs and visions of our clients.

Quality and Reliability: Commitment to high-quality materials, skilled workmanship, and delivering projects on time and within budget.

Website Requirements:

Clean, professional design reflecting the quality and reliability of our services.

User-friendly navigation to easily access information about our services, portfolio, company background, and contact details.

Portfolio section showcasing our past projects with placeholders for images and descriptions.

Integration of a contact form, map for our location, and links to our social media accounts.

Mobile-responsive design to ensure accessibility across various devices.

Purpose of the Website:
The website aims to:

Establish an online presence and credibility in the construction industry.

Provide an informative resource about our services and past projects to potential clients.

Facilitate easy communication and inquiries through an integrated contact system.

Tone and Style:

Professional, informative, and welcoming. The website should convey trustworthiness and expertise in the construction field.

homeowners, real estate developers, and commercial clients

Construction

3 page

```html
<!DOCTYPE html>
<html lang="en">
<head>
<meta charset="utf-8">
<title>Torvin Group — Construction in London</title>
<link href="https://fonts.googleapis.com/css2?family=Roboto:wght@400;500;700;900&display=swap" rel="stylesheet">
<style>
:root{
  --teal:#1d6f6f;
  --teal-dark:#134c4f;
  --copper:#b27a3c;
  --ink:#1e2a2e;
  --muted:#5f6b6e;
  --soft:#eef4f4;
  --cream:#f8efe4;
  --line:#dfe6e6;
  --white:#ffffff;
}
*{box-sizing:border-box;margin:0;padding:0}
html,body{width:1200px;height:4260px;overflow:hidden}
body{font-family:"Roboto",Arial,sans-serif;color:var(--ink);background:var(--white);position:relative}
section,header,footer{position:absolute;left:0;width:1200px}
.abs{position:absolute}
.btn{display:inline-block;font-weight:700;font-size:15px;letter-spacing:.5px;color:#fff;padding:14px 26px;border-radius:4px}
.btn-copper{background:var(--copper)}
.btn-teal{background:var(--teal)}

/* header */
.site-header{top:0;height:80px;background:#fff;box-shadow:0 2px 8px rgba(0,0,0,.06);z-index:5}
.brand{position:absolute;display:flex;align-items:center;gap:10px;font-weight:900;font-size:26px;color:var(--teal-dark);letter-spacing:1px}
.brand-square{width:26px;height:26px;background:var(--copper)}
.site-header .brand{left:110px;top:24px}
.nav{position:absolute;left:470px;top:30px;display:flex;gap:44px;font-size:17px;font-weight:500;color:var(--ink)}
.phone-pill{position:absolute;right:110px;top:20px;height:40px;padding:0 22px 0 10px;border:1px solid var(--line);border-radius:20px;display:flex;align-items:center;gap:10px;font-weight:700;color:var(--teal-dark)}
.phone-pill .dot{width:26px;height:26px;border-radius:50%;background:var(--copper);display:flex;align-items:center;justify-content:center}

/* hero */
.hero{top:80px;height:680px;background:linear-gradient(110deg,#2b2a2a 0%,#5a4d45 45%,#8b8f93 100%)}
.hero-title{left:110px;top:120px;font-size:56px;line-height:64px;font-weight:900;color:#fff;width:380px}
.hero-sub{left:110px;top:340px;width:430px;font-size:21px;line-height:30px;font-weight:700;color:#fff}
.hero .btn{position:absolute;left:110px;top:450px}
.hero-graphic{left:620px;top:70px;width:430px;height:430px;border-radius:50%;background:radial-gradient(circle,rgba(255,255,255,.22) 0%,rgba(255,255,255,.08) 70%,rgba(255,255,255,0) 100%)}

/* welcome */
.welcome{top:760px;height:600px}
.welcome-photo{left:120px;top:100px;width:380px;height:420px;background:linear-gradient(160deg,#d7d0c6,#a99c8b);border-radius:2px}
.welcome-title{left:590px;top:110px;font-size:28px;font-weight:700;color:var(--ink)}
.welcome-text{left:590px;top:170px;width:440px;font-size:17px;line-height:27px;color:var(--muted)}
.welcome .btn{position:absolute;left:590px;top:370px}
.stats{left:390px;top:478px;display:flex;gap:14px}
.stat{background:#fff;box-shadow:0 4px 14px rgba(0,0,0,.1);width:160px;height:82px;text-align:center;padding-top:10px}
.stat b{display:block;font-size:34px;font-weight:900;color:var(--teal-dark)}
.stat span{font-size:12px;color:var(--muted)}
.deco-shape{right:0;top:80px;width:150px;height:300px;background:var(--soft)}

/* why */
.why{top:1360px;height:560px}
.section-title{font-size:32px;font-weight:700;color:var(--ink)}
.why .section-title{left:0;width:1200px;text-align:center;top:80px}
.why-cards{left:112px;top:160px;display:flex;gap:20px}
.why-card{width:312px;height:330px;border:1px solid var(--line);background:#fff;text-align:center;padding:30px 28px;box-shadow:0 4px 14px rgba(0,0,0,.06)}
.why-card.featured{background:#eaf3f2}
.why-icon{width:90px;height:90px;border-radius:50%;margin:0 auto 24px;background:linear-gradient(140deg,#d6a66c,#2a7c7b)}
.why-card h3{font-size:22px;font-weight:700;margin-bottom:14px}
.why-card p{font-size:14px;line-height:22px;color:var(--muted)}

/* services */
.services{top:1980px;height:1000px;background:var(--soft)}
.services .section-title{left:0;width:1200px;text-align:center;top:70px}
.services-intro{left:280px;top:130px;width:640px;text-align:center;font-size:18px;line-height:28px;color:var(--muted)}
.service-grid{left:112px;top:252px;display:grid;grid-template-columns:240px 232px 236px 236px;grid-auto-rows:270px 300px;column-gap:12px;row-gap:26px}
.service-tile{position:relative;overflow:hidden}
.service-tile span{position:absolute;left:18px;bottom:18px;color:#fff;font-size:24px;font-weight:500;line-height:28px;text-shadow:0 1px 3px rgba(0,0,0,.5)}
.t1{background:linear-gradient(160deg,#5b4a3d,#1f2b33)}
.t2{background:linear-gradient(160deg,#6e8795,#324a5a)}
.t3{background:linear-gradient(160deg,#b7c2c8,#596a76)}
.t4{background:linear-gradient(160deg,#c8cbc9,#6e7b82)}
.t5{background:linear-gradient(160deg,#7b6a58,#2f3a40)}
.t6{background:linear-gradient(160deg,#8a97a0,#3c4a52)}
.t7{background:linear-gradient(160deg,#e8eaea,#9aa6ac)}
.t8{background:linear-gradient(160deg,#9b7d64,#5b4f47)}

/* testimonials */
.testimonials{top:3040px;height:460px}
.testimonials .section-title{left:110px;top:20px}
.testimonials-intro{left:110px;top:76px;width:620px;font-size:17px;line-height:26px;color:var(--muted)}
.arrows{right:110px;top:60px;display:flex;gap:14px}
.quote-cards{left:112px;top:180px;display:flex;gap:40px}
.quote-card{width:310px;height:240px;background:#fff;box-shadow:0 4px 18px rgba(0,0,0,.09);padding:26px 28px}
.quote-head{display:flex;align-items:center;gap:16px;margin-bottom:20px}
.avatar{width:52px;height:52px;border-radius:50%;background:linear-gradient(140deg,#c9b8a6,#6b5a4c)}
.quote-head b{display:block;font-size:18px;font-weight:500}
.quote-head small{font-size:13px;color:var(--muted)}
.quote-card p{font-size:14px;line-height:22px;color:var(--muted)}
.testi-deco{left:0;top:300px;width:80px;height:180px;background:var(--soft)}

/* contact */
.contact{top:3540px;height:350px;background:var(--cream);overflow:hidden}
.contact-title{left:110px;top:50px;font-size:32px;font-weight:700}
.contact-lead{left:110px;top:104px;font-size:30px;font-weight:700;color:var(--copper)}
.contact-text{left:110px;top:160px;width:520px;font-size:18px;line-height:28px;color:var(--muted)}
.contact .btn{position:absolute;left:110px;top:250px}
.contact-photo{left:640px;top:0;width:560px;height:350px;background:linear-gradient(100deg,var(--cream) 0%,#e2c6a4 35%,#b99474 100%)}

/* footer */
.site-footer{top:3890px;height:370px;background:#fff}
.site-footer .brand{left:110px;top:150px;font-size:30px}
.footer-divider{left:360px;top:40px;width:1px;height:300px;background:var(--line)}
.footer-divider.two{left:790px}
.footer-col h4{font-size:18px;font-weight:700;margin-bottom:24px}
.footer-links{left:460px;top:40px}
.footer-links li{list-style:none;display:flex;align-items:center;gap:12px;font-size:16px;color:var(--muted);margin-bottom:18px}
.footer-links li i{width:10px;height:10px;border-radius:50%;border:2px solid var(--teal)}
.footer-contact{left:845px;top:40px}
.contact-item{display:flex;gap:16px;margin-bottom:22px}
.contact-item svg{flex:none;margin-top:2px}
.contact-item b{display:block;font-size:15px;font-weight:500}
.contact-item span{font-size:15px;color:var(--muted)}
</style>
</head>
<body>

<header class="site-header">
  <div class="brand"><span class="brand-square"></span>TORVIN GROUP</div>
  <nav class="nav">
    <svg width="18" height="18" viewBox="0 0 24 24" style="margin-top:1px"><path d="M3 11L12 3l9 8v10h-6v-6H9v6H3z" fill="var(--ink)"/></svg>
    <span>About</span><span>Services</span><span>Portfolio</span><span>Contact</span>
  </nav>
  <div class="phone-pill"><span class="dot"><svg width="14" height="14" viewBox="0 0 24 24"><path d="M6.6 10.8a15 15 0 0 0 6.6 6.6l2.2-2.2c.3-.3.7-.4 1-.2 1.1.4 2.3.6 3.6.6.6 0 1 .4 1 1V20c0 .6-.4 1-1 1A17 17 0 0 1 3 4c0-.6.4-1 1-1h3.5c.6 0 1 .4 1 1 0 1.3.2 2.5.6 3.6.1.3 0 .7-.2 1z" fill="#fff"/></svg></span>(020) 555 0142</div>
</header>

<section class="hero" role="img" aria-label="Photo of a tradesman working on electrical wiring">
  <h1 class="abs hero-title">Building Your Dreams Into Reality</h1>
  <p class="abs hero-sub">Expert Craftsmanship Meets Unmatched Reliability in the Heart of London</p>
  <a class="btn btn-copper">LEARN MORE</a>
  <div class="abs hero-graphic" role="img" aria-label="Illustration of construction service icons arranged in a circle"></div>
</section>

<section class="welcome">
  <div class="abs deco-shape"></div>
  <div class="abs welcome-photo" role="img" aria-label="Photo of a smiling family sitting on the floor of their new home"></div>
  <h2 class="abs welcome-title">WELCOME TO TORVIN GROUP</h2>
  <p class="abs welcome-text">Where Construction Meets Excellence. Based in London, we are committed to transforming your spaces into exceptional places. Our team is dedicated to delivering the highest quality in every project, attending to every detail with precision and care.</p>
  <a class="btn btn-teal">LEARN MORE</a>
  <div class="abs stats">
    <div class="stat"><b>30</b><span>Years of Experience</span></div>
    <div class="stat"><b>12K+</b><span>Projects Completed</span></div>
    <div class="stat"><b>10K+</b><span>Happy Clients</span></div>
    <div class="stat"><b>10</b><span>Year Warranty</span></div>
  </div>
</section>

<section class="why">
  <h2 class="abs section-title">WHY CHOOSE US</h2>
  <div class="abs why-cards">
    <div class="why-card"><div class="why-icon" role="img" aria-label="Team expertise icon"></div><h3>Our Expertise</h3><p>Leveraging over 30 years of experience, Torvin Group stands as a beacon of excellence in the construction industry. We handle each project, big or small.</p></div>
    <div class="why-card featured"><div class="why-icon" role="img" aria-label="Quality badge icon"></div><h3>Quality Assurance</h3><p>Quality is not just a promise, but a practice. Meticulous attention to detail ensures flawless finishes and durable structures, bringing long lasting value.</p></div>
    <div class="why-card"><div class="why-icon" role="img" aria-label="Certificate icon"></div><h3>Certified Excellence</h3><p>Your safety and satisfaction are our top priorities. We provide electrical certificates and adhere to the highest industry standards, offering peace of mind.</p></div>
  </div>
</section>

<section class="services">
  <h2 class="abs section-title">OUR SERVICES</h2>
  <p class="abs services-intro">Tailored to Your Needs. Discover how we can bring your vision to life, covering every aspect of construction from the initial design to the final touches</p>
  <div class="abs service-grid">
    <div class="service-tile t1" role="img" aria-label="Photo of electrical work"><span>Electrical<br>Work</span></div>
    <div class="service-tile t2" role="img" aria-label="Photo of a decorator painting a wall"><span>Painting and<br>Decorating</span></div>
    <div class="service-tile t3" role="img" aria-label="Photo of plastering a wall"><span>Plastering</span></div>
    <div class="service-tile t4" role="img" aria-label="Photo of plumbing under a sink"><span>Plumbing</span></div>
    <div class="service-tile t5" role="img" aria-label="Photo of a carpenter at work"><span>Carpentry</span></div>
    <div class="service-tile t6" role="img" aria-label="Photo of a fitted kitchen"><span>Kitchen &amp; Bathroom<br>Installations</span></div>
    <div class="service-tile t7" role="img" aria-label="Photo of a bright converted loft"><span>Loft Conversions</span></div>
    <div class="service-tile t8" role="img" aria-label="Photo of a brick house extension"><span>Extensions</span></div>
  </div>
</section>

<section class="testimonials">
  <div class="abs testi-deco"></div>
  <h2 class="abs section-title">TESTIMONIALS</h2>
  <p class="abs testimonials-intro">Tailored to Your Needs. Discover how we can bring your vision to life, covering every aspect of construction from the initial design to t</p>
  <div class="abs arrows">
    <svg width="28" height="20" viewBox="0 0 28 20"><path d="M26 10H3M10 3L3 10l7 7" fill="none" stroke="var(--teal)" stroke-width="3"/></svg>
    <svg width="28" height="20" viewBox="0 0 28 20"><path d="M2 10h23M18 3l7 7-7 7" fill="none" stroke="var(--teal)" stroke-width="3"/></svg>
  </div>
  <div class="abs quote-cards">
    <div class="quote-card"><div class="quote-head"><div class="avatar" role="img" aria-label="Client portrait"></div><div><b>Daniel Rhodes</b><small>Designer</small></div></div><p>The team finished our kitchen on time and on budget. Every detail was handled with care, and the site was left spotless each day. We would gladly hire them again.</p></div>
    <div class="quote-card"><div class="quote-head"><div class="avatar" role="img" aria-label="Client portrait"></div><div><b>Daniel Rhodes</b><small>Designer</small></div></div><p>From the first visit to the final walkthrough, communication was clear and friendly. Our loft conversion feels like a brand new floor of the house. Truly great work.</p></div>
    <div class="quote-card"><div class="quote-head"><div class="avatar" role="img" aria-label="Client portrait"></div><div><b>Daniel Rhodes</b><small>Designer</small></div></div><p>Reliable, tidy and skilled tradespeople. The electrical work came with full certification and the plastering finish is flawless. Highly recommended in London.</p></div>
  </div>
</section>

<section class="contact">
  <div class="abs contact-photo" role="img" aria-label="Photo of a happy family holding a cardboard roof over their heads"></div>
  <h2 class="abs contact-title">CONTACT US</h2>
  <p class="abs contact-lead">Ready to Start Your Project?</p>
  <p class="abs contact-text">Contact us today for a consultation and embark on the journey to turn your construction dreams into a stunning reality</p>
  <a class="btn btn-teal">REQUEST A QUOTE</a>
</section>

<footer class="site-footer">
  <div class="brand"><span class="brand-square"></span>TORVIN GROUP</div>
  <div class="abs footer-divider"></div>
  <div class="abs footer-divider two"></div>
  <div class="abs footer-col footer-links">
    <h4>LINKS</h4>
    <ul>
      <li><i></i>Home</li><li><i></i>About Us</li><li><i></i>Services</li><li><i></i>Projects</li><li><i></i>Contact Us</li>
    </ul>
  </div>
  <div class="abs footer-col footer-contact">
    <h4>CONTACT</h4>
    <div class="contact-item"><svg width="18" height="22" viewBox="0 0 24 24"><path d="M12 2a7 7 0 0 0-7 7c0 5 7 13 7 13s7-8 7-13a7 7 0 0 0-7-7zm0 9.5A2.5 2.5 0 1 1 12 6.5a2.5 2.5 0 0 1 0 5z" fill="var(--ink)"/></svg><div><b>Address:</b><span>48 Elmfield Road</span></div></div>
    <div class="contact-item"><svg width="18" height="22" viewBox="0 0 24 24"><path d="M6.6 10.8a15 15 0 0 0 6.6 6.6l2.2-2.2c.3-.3.7-.4 1-.2 1.1.4 2.3.6 3.6.6.6 0 1 .4 1 1V20c0 .6-.4 1-1 1A17 17 0 0 1 3 4c0-.6.4-1 1-1h3.5c.6 0 1 .4 1 1 0 1.3.2 2.5.6 3.6.1.3 0 .7-.2 1z" fill="var(--ink)"/></svg><div><b>Phone:</b><span>(020) 555 0178</span></div></div>
    <div class="contact-item"><svg width="18" height="22" viewBox="0 0 24 24"><path d="M3 5h18v14H3zM3 5l9 8 9-8" fill="none" stroke="var(--ink)" stroke-width="2"/></svg><div><b>Email:</b><span>hello@torvingroup.example</span></div></div>
  </div>
</footer>

</body>
</html>
```